New Business Card Design Project

Make a kick ass business card for the Otter Cider Mug, using the designs. I also might like the 2nd place design logo on the back? Maybe all black with that? Not sure. Also, I'm cool with it being on metal, plastic, glass? or whatever for the business card. Maybe shaped like a shark? Let me know what else you need? Would like designs in the next day or so. Thank you.
Target Market(s)
Anyone that is cool
Contact Information for Business Card
Name: Daniel Forsby
Phone: 480.317.4962
inventor/creator/entrepreneur/owner
www.theottercidermug.example
social media links
https://www.facebook.com/theottercidermug
https://twitter.com/otter_cider
https://www.instagram.com/theottercidermug/
I'll get the Pinterest one soon
Colors
Designer to choose colors to be used in the design.
Requirements
Must have
- The Otter Cider Mug
- www.theottercidermug.example
- social media tags?
- My logos and picture/photo of wine glass
Nice to have
- Maybe shaped like a wine glass or shark
- I'll let you decide but my same colors from my website would be nice

```html
<!DOCTYPE html>
<html lang="en">
<head>
<meta charset="utf-8">
<title>Otter Cider Mug – Business Cards</title>
<link rel="stylesheet" href="https://fonts.googleapis.com/css2?family=Poppins:wght@300;400;600;700&display=swap">
<style>
  :root{
    --stage:#2b2c2f;
    --card-black:#121212;
    --card-white:#ffffff;
    --brand-red:#c1444b;
    --brand-gray:#8a8a8a;
    --gold:#e2b33c;
    --text-light:#e9e9e9;
  }
  *{margin:0;padding:0;box-sizing:border-box}
  html,body{width:1200px;height:900px;overflow:hidden}
  body{
    background:var(--stage);
    font-family:"Poppins",sans-serif;
    display:flex;align-items:center;justify-content:center;gap:60px;
  }
  .card{
    width:500px;height:286px;border-radius:4px;position:relative;overflow:hidden;
    box-shadow:0 14px 30px rgba(0,0,0,.45);
  }
  /* back side */
  .card-back{background:var(--card-black);display:flex;align-items:center;padding:0 34px}
  .card-back .brand-mark{
    width:190px;display:flex;align-items:center;gap:10px;
    color:var(--gold);font-weight:600;font-size:22px;line-height:1.15;
  }
  .card-back .brand-mark .dot{width:14px;height:14px;border-radius:50%;background:var(--gold);flex:none}
  .contact{margin-left:28px;color:var(--text-light);font-size:14px;line-height:1.45}
  .contact .person{font-weight:700;font-size:19px;color:#fff}
  .contact .role{font-weight:300;font-size:13px;margin-bottom:12px}
  .contact .email{font-weight:600;color:#fff}
  .contact .web{font-weight:300}
  /* front side */
  .card-front{background:var(--card-white);display:flex;flex-direction:column}
  .card-front .top{flex:0 0 150px;display:flex;align-items:flex-end;padding:0 24px 14px}
  .wordmark{font-weight:300;font-size:44px;color:var(--brand-gray);letter-spacing:-.5px;white-space:nowrap}
  .band{flex:1;background:var(--brand-red);display:flex;align-items:center;justify-content:space-between;padding:0 24px}
  .social{display:flex;align-items:center;gap:6px;color:#fff;font-size:12.5px;font-weight:400}
  .social .icon{width:15px;height:15px;border-radius:50%;background:#fff;flex:none}
</style>
</head>
<body>
  <section class="card card-back" aria-label="Card back">
    <div class="brand-mark"><span class="dot"></span><span>Otter Cider Mug</span></div>
    <div class="contact">
      <p class="person">Daniel Forsby</p>
      <p class="role">Inventor/creator/entrepreneur/owner</p>
      <p class="phone">480.317.4962</p>
      <p class="email">email@theottercidermug.example</p>
      <p class="web">www.theottercidermug.example</p>
    </div>
  </section>

  <section class="card card-front" aria-label="Card front">
    <div class="top"><span class="wordmark">Otter Cider Mug</span></div>
    <div class="band">
      <div class="social"><span class="icon"></span><span class="icon"></span><span>theottercidermug</span></div>
      <div class="social"><span class="icon"></span><span>otter_cider</span></div>
      <div class="social"><span class="icon"></span><span>ottercider</span></div>
    </div>
  </section>
</body>
</html>
```